Wine Label Design for Marrick Estate

I need a front and back label for a new wine I am making. I am looking for a classic, elegant and serious wine label. I would like the label to be white with blue and black writing. The blue will be the distinction in the label. The color of blue will be unique and catch the eye. The font of the writing will be unique and could also serve as the brand image for Marrick Estate. The label can have a design but should be simple and distinct. I envision the paper quality of the label to textured, high quality and add to the overall image of the label.
The label will be timeless. The price of this wine will be $85.00 a bottle, and the label should match a higher priced wine. This wine is family owned and operated.
The writing on the front and back label will be:

FRONT Label-

Marrick Estate

Howell Mountain

Napa Valley

2022 Cabernet Sauvignon

Back Label-

Cellared and Bottled by Marrick Estate, Angwin, CA 94508

GOVERNMENT WARNING: (1) According to the Surgeon General, women should not drink alcoholic beverages during pregnancy because of the risk of birth defects. (2) Consumption of alcoholic beverages impairs your ability to drive a car or operate machinery, and may cause health problems.

Alc. 14.5% by Vol.

750 ml

Contains Sulfites

```html
<!DOCTYPE html>
<html lang="en">
<head>
<meta charset="utf-8">
<title>Marrick Estate – Howell Mountain Cabernet Sauvignon Label</title>
<link href="https://fonts.googleapis.com/css2?family=Playfair+Display:wght@800;900&family=Montserrat:wght@500;600;700&family=Oswald:wght@400&display=swap" rel="stylesheet">
<style>
  :root {
    --backdrop: #dcdcdc;
    --paper: #f3f3f1;
    --paper-shade: #e9e9e6;
    --navy: #14295c;
    --ink: #111111;
    --white: #ffffff;
  }
  * { box-sizing: border-box; margin: 0; padding: 0; }
  html, body {
    width: 1200px; height: 1200px; overflow: hidden;
    background: var(--backdrop);
  }
  .label {
    position: absolute; left: 210px; top: 80px;
    width: 780px; height: 1040px;
    background:
      radial-gradient(circle at 30% 20%, var(--paper) 0%, var(--paper-shade) 140%);
    box-shadow: 0 2px 6px rgba(0,0,0,0.12);
    overflow: hidden;
  }
  .label-frame { position: absolute; inset: 0; }
  .brand {
    position: absolute; left: 0; right: 0; top: 150px;
    text-align: center;
    font-family: "Playfair Display", serif;
    font-weight: 900; color: var(--ink);
    line-height: 1;
  }
  .brand-mark {
    display: block; width: 14px; height: 14px;
    margin: 0 auto 28px; background: var(--navy);
  }
  .brand-name { display: block; font-size: 128px; letter-spacing: -2px; }
  .brand-sub { display: block; font-size: 86px; margin-top: 6px; letter-spacing: -1px; }
  .mountain-art {
    position: absolute; left: 120px; top: 405px;
    width: 545px; height: 150px;
    background: linear-gradient(to bottom, rgba(20,41,92,0.15), var(--navy));
  }
  .region-band {
    position: absolute; left: 0; right: 0; top: 555px; height: 190px;
    background: var(--navy); color: var(--white);
  }
  .region-name {
    position: absolute; left: 0; right: 0; top: 38px;
    text-align: center;
    font-family: "Montserrat", sans-serif; font-weight: 700;
    font-size: 54px; line-height: 58px; letter-spacing: 6px;
  }
  .band-note {
    position: absolute; top: 100px;
    font-family: "Oswald", sans-serif; font-size: 22px; letter-spacing: 1px;
  }
  .band-note.left { left: 116px; }
  .band-note.right { right: 118px; }
  .vintage {
    position: absolute; left: 0; right: 0; top: 776px;
    text-align: center;
    font-family: "Montserrat", sans-serif; font-weight: 700;
    font-size: 64px; line-height: 70px; color: var(--navy);
  }
  .vintage-rule {
    position: absolute; top: 812px; height: 2px; width: 100px;
    background: var(--navy);
  }
  .vintage-rule.left { left: 164px; }
  .vintage-rule.right { left: 520px; }
  .varietal {
    position: absolute; left: 0; right: 0; top: 850px;
    text-align: center;
    font-family: "Montserrat", sans-serif; font-weight: 600;
    font-size: 32px; color: var(--ink); letter-spacing: 0.5px;
  }
  .appellation {
    position: absolute; left: 245px; top: 922px;
    width: 300px; height: 40px;
    border: 2px solid var(--navy); border-radius: 20px;
    text-align: center;
    font-family: "Montserrat", sans-serif; font-weight: 500;
    font-size: 20px; line-height: 36px; letter-spacing: 7px;
    color: var(--navy);
  }
</style>
</head>
<body>
  <div class="label">
    <svg class="label-frame" width="780" height="1040" viewBox="0 0 780 1040">
      <polygon points="53,24 727,24 757,54 757,986 727,1016 53,1016 23,986 23,54"
               fill="none" stroke="var(--navy)" stroke-width="3"/>
    </svg>

    <h1 class="brand">
      <span class="brand-mark"></span>
      <span class="brand-name">MARRICK</span>
      <span class="brand-sub">ESTATE</span>
    </h1>

    <div class="mountain-art" role="img" aria-label="Navy mountain peak illustration with white snow streaks"></div>

    <div class="region-band">
      <span class="band-note left">ESTD</span>
      <p class="region-name">HOWELL<br>MOUNTAIN</p>
      <span class="band-note right">2024</span>
    </div>

    <span class="vintage-rule left"></span>
    <p class="vintage">2022</p>
    <span class="vintage-rule right"></span>
    <p class="varietal">CABERNET SAUVIGNON</p>

    <p class="appellation">NAPA VALLEY</p>
  </div>
</body>
</html>
```